Banner Ad Design Project for responsive website

Looking to update the main banner on my website www.vowlantern.example but it will be for our new responsive website, you can see here http://www.vowlantern.example/dev/
Banner should be 300 px high by1920 pix wide
Please contact me with any questions
Should include:
All the text from the existing banner ie
Bridal Show
THE FIRST 50 BRIDES WILL GET A CHANCE TO WIN $25000
Honeymoon Cruise Giveaway
"Pick Your Perfect Gown" casting call
Banner should be 1920 pix wide
Final delivery will require layered psd file and all fonts

Target Market(s)

Brides

Industry/Entity Type

Call

Requirements
Must have
• All the text from the existing banner ie
• Bridal Show
• THE FIRST 50 BRIDES WILL GET A CHANCE TO WIN $25000
• Honeymoon Cruise Giveaway
• "Pick Your Perfect Gown" casting call
• Banner should be 1920 pix wide
Nice to have
• The look and feel of our postcard, see attached
Should not have
• Any specifics to any date/time/location as the banner will be online all the time and the specifics for each show will be different

```html
<!DOCTYPE html>
<html lang="en">
<head>
<meta charset="utf-8">
<title>Bridal Show Casting Call Banner</title>
<link rel="stylesheet" href="https://fonts.googleapis.com/css2?family=Great+Vibes&family=Arimo:wght@400;700&family=Archivo+Black&display=swap">
<style>
  :root {
    --page-bg: #eceae6;
    --banner-bg: #ffffff;
    --blush-tint: #fbeef1;
    --script-green: #1d7a22;
    --bold-green: #16701b;
    --script-blue: #4b93dc;
    --ink: #111111;
    --rule-blue: #b9d7ee;
    --ring-grey: #d9d9d9;
    --photo-green: #6fae3c;
    --photo-skin: #e9c2a8;
    --photo-white: #f6f4f2;
    --sea-blue: #2f5f92;
    --sky-blue: #a9c9e6;
  }
  * { margin: 0; padding: 0; box-sizing: border-box; }
  html, body { width: 1200px; height: 900px; overflow: hidden; }
  body { background: var(--page-bg); position: relative; font-family: "Arimo", Arial, sans-serif; }

  .banner {
    position: absolute; left: 40px; top: 208px;
    width: 1120px; height: 484px; overflow: hidden;
    background:
      radial-gradient(ellipse 260px 180px at 120px 120px, var(--blush-tint), transparent 70%),
      radial-gradient(ellipse 300px 200px at 560px 380px, var(--blush-tint), transparent 70%),
      var(--banner-bg);
    box-shadow: 0 10px 30px rgba(0,0,0,.18);
  }

  .bell-ornament {
    position: absolute; border-radius: 40%;
    background: radial-gradient(circle, rgba(29,122,34,.18), rgba(29,122,34,0) 70%);
  }
  .bell-ornament--left { left: 65px; top: 4px; width: 85px; height: 60px; }
  .bell-ornament--right { left: 565px; top: 9px; width: 62px; height: 44px; }

  .show-title {
    position: absolute; left: 0; width: 720px; top: 10px; text-align: center;
    font-family: "Great Vibes", cursive; font-size: 84px; color: var(--script-green);
    line-height: 1.1; font-weight: 400;
  }
  .casting-call {
    position: absolute; left: 0; width: 740px; top: 94px; text-align: center;
    font-size: 25px; color: var(--ink);
  }
  .tagline {
    position: absolute; left: 0; width: 740px; top: 132px; text-align: center;
    font-size: 25px; color: var(--ink);
  }
  .tagline .script-word {
    font-family: "Great Vibes", cursive; color: var(--script-blue); font-size: 34px;
  }

  .rule { position: absolute; height: 1px; background: var(--rule-blue); }
  .rule--top { left: 59px; width: 580px; top: 191px; }
  .rule--bottom { left: 57px; width: 650px; top: 334px; }

  .prize-offer {
    position: absolute; left: 28px; width: 660px; top: 214px; text-align: center;
    font-size: 36px; line-height: 34px; color: var(--ink); letter-spacing: 3px;
  }
  .prize-offer .highlight {
    font-family: "Archivo Black", "Arial Black", sans-serif; color: var(--bold-green);
    letter-spacing: 1px;
  }
  .prize-offer .amount { font-size: 38px; }

  .cruise-badge { position: absolute; left: 532px; top: 296px; width: 220px; height: 180px; }
  .bride-photo { position: absolute; left: 0; top: 0; width: 1120px; height: 484px; }
</style>
</head>
<body>
  <section class="banner">
    <svg class="bride-photo" viewBox="0 0 1120 484">
      <defs>
        <linearGradient id="brideTones" x1="0" y1="0" x2="0.3" y2="1">
          <stop offset="0" stop-color="var(--photo-green)"/>
          <stop offset="0.35" stop-color="var(--photo-skin)"/>
          <stop offset="0.75" stop-color="var(--photo-white)"/>
          <stop offset="1" stop-color="var(--photo-white)"/>
        </linearGradient>
      </defs>
      <circle cx="1072" cy="242" r="350" fill="var(--ring-grey)"/>
      <circle cx="1072" cy="242" r="344" fill="url(#brideTones)" role="img" aria-label="Photo of a smiling bride in a tiara, veil and white gown"/>
    </svg>

    <div class="bell-ornament bell-ornament--left" role="img" aria-label="Green wedding bells ornament"></div>
    <div class="bell-ornament bell-ornament--right" role="img" aria-label="Green wedding bells ornament"></div>

    <h1 class="show-title">Bridal Show</h1>
    <p class="casting-call">Casting Call</p>
    <p class="tagline">Pick Your <span class="script-word">Perfect</span> <span class="script-word">Gown</span></p>

    <div class="rule rule--top"></div>
    <p class="prize-offer">
      THE FIRST <span class="highlight">50</span> BRIDES WILL<br>
      GET A CHANCE TO WIN<br>
      <span class="highlight amount">$25,000</span>
    </p>
    <div class="rule rule--bottom"></div>

    <svg class="cruise-badge" viewBox="0 0 220 180">
      <defs>
        <path id="badgeArc" d="M18 128 A92 92 0 0 1 202 128"/>
        <linearGradient id="seaTones" x1="0" y1="0" x2="0" y2="1">
          <stop offset="0" stop-color="var(--sky-blue)"/>
          <stop offset="0.55" stop-color="#e8eef4"/>
          <stop offset="1" stop-color="var(--sea-blue)"/>
        </linearGradient>
      </defs>
      <text font-family="Great Vibes, cursive" font-size="24" fill="var(--script-green)">
        <textPath href="#badgeArc" startOffset="50%" text-anchor="middle">Honeymoon Cruise Giveaway</textPath>
      </text>
      <circle cx="110" cy="126" r="48" fill="url(#seaTones)" role="img" aria-label="Photo of a cruise ship at sea"/>
    </svg>
  </section>
</body>
</html>
```